New Print Material Needed for Renovation Company

We are looking to update our current Print Material to reflect the current process we offer to our clients. A lot of the information is also outdated along with many of the photos that are currently being used. We are a renovation company that specializes in residential and commercial renovations and custom builds.This project is MULTIPLE pages. We will pay the chosen designer an extra fee for the designing 3-4 additional pages that are similar to the chosen design. Attached is our current Print Material. We are hoping to update the look of them and some of the messaging. Our current company colors are white, blue and light grey and it will remain that way.

Industry/Entity Type

Construction Company

Font styles to use
Sans Serif

Colors
3176b5
ffffff

Requirements
Must have
• Easy to explain the process
• Easy to read and understand let alone
• Easy to navigate
Nice to have
• As much creativity as possible
Should not have
• no confusing text
• no confusing layout

```html
<!DOCTYPE html>
<html lang="en">
<head>
<meta charset="utf-8">
<title>Master Builder Timeline</title>
<link href="https://fonts.googleapis.com/css2?family=Montserrat:wght@800;900&family=Roboto+Condensed:wght@700;800&family=Roboto+Mono:wght@400;500;600&display=swap" rel="stylesheet">
<style>
  :root {
    --royal: #2442d6;
    --brand: #3176b5;
    --ink: #0d1426;
    --paper: #ffffff;
    --design-bg: #effbfd;
    --plan-bg: #e2f7fb;
    --build-bg: #d2f1f8;
    --card-bg: #f3fcfe;
    --card-line: #bfeaf3;
    --start-line: #7f95e6;
  }
  * { box-sizing: border-box; margin: 0; padding: 0; }
  html, body { width: 929px; height: 1200px; overflow: hidden; background: var(--paper); }
  .timeline { position: relative; width: 929px; height: 1200px; font-family: "Roboto Mono", monospace; color: var(--ink); }
  .band { position: absolute; left: 30px; width: 870px; }
  .band--design { top: 23px; height: 493px; background: var(--design-bg); }
  .band--plan { top: 516px; height: 326px; background: var(--plan-bg); }
  .band--build { top: 842px; height: 330px; background: var(--build-bg); }
  .band-label {
    position: absolute; left: 50px; transform: translate(-50%, -50%) rotate(-90deg);
    font-family: "Roboto Condensed", sans-serif; font-weight: 800; font-size: 46px; line-height: 46px;
    letter-spacing: 1px; color: var(--royal); white-space: nowrap;
  }
  .header-mark { position: absolute; left: 83px; top: 61px; width: 54px; height: 54px; border-radius: 50%; background: var(--royal); }
  .title {
    position: absolute; left: 153px; top: 64px; font-family: "Montserrat", sans-serif;
    font-weight: 800; font-size: 35px; line-height: 44px; letter-spacing: 0; color: var(--ink); white-space: nowrap;
  }
  .company {
    position: absolute; left: 748px; top: 65px; width: 110px; height: 37px; background: var(--royal);
    color: var(--paper); font-family: "Roboto Mono", monospace; font-weight: 600; font-size: 10px;
    line-height: 12px; display: flex; align-items: center; padding-left: 10px;
  }
  .start-date {
    position: absolute; left: 109px; top: 141px; width: 264px; height: 41px; border: 1.5px solid var(--start-line);
    background: var(--paper); color: var(--royal); font-size: 17px; padding: 9px 14px;
  }
  .step { position: absolute; width: 218px; height: 274px; background: var(--card-bg); border: 2px solid var(--card-line); }
  .step--build { border: 1.5px solid var(--royal); }
  .step-number {
    position: absolute; right: 8px; top: 14px; transform-origin: right top; transform: rotate(90deg) translate(100%, 0);
    font-family: "Roboto Condensed", sans-serif; font-weight: 800; font-size: 48px; line-height: 40px; color: var(--royal);
  }
  .step-body { position: absolute; left: 13px; right: 10px; top: 96px; }
  .step-title { font-size: 16px; font-weight: 500; line-height: 19px; letter-spacing: 0.3px; }
  .step-text { font-size: 13px; font-weight: 500; line-height: 19px; margin-top: 1px; }
  .step-duration { position: absolute; left: 13px; bottom: 18px; font-size: 16px; font-weight: 500; color: var(--royal); }
  .connectors { position: absolute; left: 0; top: 0; }
</style>
</head>
<body>
<main class="timeline">
  <div class="band band--design"><span class="band-label" style="top:383px">DESIGN</span></div>
  <div class="band band--plan"><span class="band-label" style="top:245px">PLAN</span></div>
  <div class="band band--build"><span class="band-label" style="top:233px">BUILD</span></div>

  <div class="header-mark"></div>
  <h1 class="title">MASTER BUILDER TIMELINE</h1>
  <div class="company">Northfield<br>Builders</div>
  <div class="start-date">Start Date:</div>

  <svg class="connectors" width="929" height="1200" viewBox="0 0 929 1200" fill="none" stroke="#2442d6" stroke-width="1.6">
    <g>
      <path d="M342 343H372M364 336L372 343L364 350"/>
      <path d="M608 343H638M630 336L638 343L630 350"/>
      <path d="M342 670H372M364 663L372 670L364 677"/>
      <path d="M608 670H638M630 663L638 670L630 677"/>
      <path d="M342 998H372M364 991L372 998L364 1005"/>
      <path d="M608 998H638M630 991L638 998L630 1005"/>
      <path d="M858 488V506H124V524M118 517L124 524L130 517"/>
      <path d="M858 818V836H124V852M118 845L124 852L130 845"/>
    </g>
  </svg>

  <section class="step" style="left:115px;top:206px">
    <span class="step-number">1.</span>
    <div class="step-body"><h2 class="step-title">Initial Design Meeting</h2><p class="step-text">The first step of the design process is to confirm the design concept you have envisioned.</p></div>
    <span class="step-duration">1-2 weeks</span>
  </section>
  <section class="step" style="left:381px;top:206px">
    <span class="step-number">2.</span>
    <div class="step-body"><h2 class="step-title">Second Design Meeting</h2><p class="step-text">Our designers work directly with you to ensure the measurements line up with your design ideas.</p></div>
    <span class="step-duration">1-2 weeks</span>
  </section>
  <section class="step" style="left:648px;top:206px">
    <span class="step-number">3.</span>
    <div class="step-body"><h2 class="step-title">Final Design Meeting</h2><p class="step-text">Any last minute or final revisions will be completed within 3 days of this meeting.</p></div>
    <span class="step-duration">1-3 weeks</span>
  </section>

  <section class="step" style="left:115px;top:534px">
    <span class="step-number">4.</span>
    <div class="step-body"><h2 class="step-title">Material Selection</h2><p class="step-text">Our material selection coordinator will work with you to ensure all the right materials.</p></div>
    <span class="step-duration">1-4 weeks</span>
  </section>
  <section class="step" style="left:381px;top:534px">
    <span class="step-number">5.</span>
    <div class="step-body"><h2 class="step-title">Engineer Drawings</h2><p class="step-text">The final permit drawings will be sent to engineers to ensure structural integrity.</p></div>
    <span class="step-duration">2-4 weeks</span>
  </section>
  <section class="step" style="left:648px;top:534px">
    <span class="step-number">6.</span>
    <div class="step-body"><h2 class="step-title">Building Permit Plans</h2><p class="step-text">Permit drawings will begin once the build has been signed and initial payments have been made.</p></div>
    <span class="step-duration">3-25 weeks</span>
  </section>

  <section class="step step--build" style="left:115px;top:862px">
    <span class="step-number">7.</span>
    <div class="step-body"><h2 class="step-title">Material Finalization</h2><p class="step-text">A lead designer will finalize any revisions you may have for your material selection.</p></div>
    <span class="step-duration">2-4 weeks</span>
  </section>
  <section class="step step--build" style="left:381px;top:862px">
    <span class="step-number">8.</span>
    <div class="step-body"><h2 class="step-title">Construction Plans</h2><p class="step-text">The drawings will be updated within 24 hours once the permits have been approved &amp; received.</p></div>
    <span class="step-duration">2-6 weeks</span>
  </section>
  <section class="step step--build" style="left:648px;top:862px">
    <span class="step-number">9.</span>
    <div class="step-body"><h2 class="step-title">Scheduling</h2><p class="step-text">All designs, dates, permits have been completed. The project is ready to get underway.</p></div>
    <span class="step-duration">2-4 weeks</span>
  </section>
</main>
</body>
</html>
```